STATIONERY and Brand ID for KelvaBank

We need a family of identical Brand guide
Call Card
Envelope
Letterhead
Poster
Brochure

It needs to have an international Fee/

The ARCHITECTURE/STRUCTURE must show the highest level of creativity

1. Call card could be two sided
2. cal card can have a a flap
3. Call card can have a curved edge

Target Market(s)

Business and bank clients

Industry/Entity Type

Bank

Requirements
Must have
• the logo atatched
• the colour scheme must be used
• There must be a common look and feel and they must have the same DNA

```html
<!DOCTYPE html>
<html lang="en">
<head>
<meta charset="utf-8">
<title>KelvaBank Poster — Banking Has Evolved</title>
<link href="https://fonts.googleapis.com/css2?family=Bebas+Neue&family=Inter:wght@400;500;700&display=swap" rel="stylesheet">
<style>
  :root {
    --navy: #243372;
    --green: #7cc31a;
    --ink: #1b1b1f;
    --grey-dark: #b9bcc4;
    --grey-mid: #d9dbe1;
    --paper-light: #f7f7f8;
    --photo-tone: #6b6a55;
    --link-dot: #3d8fe0;
    --canvas-bg: #ffffff;
  }
  * { box-sizing: border-box; margin: 0; padding: 0; }
  html, body {
    width: 1200px; height: 1200px; overflow: hidden;
    background: var(--canvas-bg);
    font-family: "Inter", sans-serif;
  }
  .poster {
    position: absolute; left: 214px; top: 62px;
    width: 768px; height: 1086px; overflow: hidden;
    background: linear-gradient(100deg, var(--grey-dark) 0%, var(--grey-mid) 40%, var(--paper-light) 75%, var(--grey-mid) 100%);
  }
  .poster__glow {
    position: absolute; left: 426px; top: 0; width: 280px; height: 1086px;
    background: radial-gradient(ellipse at 50% 45%, rgba(255,255,255,0.95) 0%, rgba(255,255,255,0.4) 55%, rgba(255,255,255,0) 100%);
  }
  .side-band { position: absolute; left: 700px; width: 23px; }
  .side-band--navy { top: 0; height: 904px; background: var(--navy); }
  .side-band--green { top: 982px; height: 104px; background: var(--green); }
  .side-link {
    position: absolute; left: 703px;
    display: flex; flex-direction: column; align-items: center; gap: 6px;
  }
  .side-link__dot { width: 16px; height: 16px; border-radius: 50%; background: var(--link-dot); }
  .side-link__text {
    writing-mode: vertical-rl;
    color: #ffffff; font-size: 11.5px; letter-spacing: 0.2px;
  }
  .side-link--one { top: 416px; }
  .side-link--two { top: 576px; }
  .portrait {
    position: absolute; left: 76px; top: 170px; width: 244px; height: 440px;
    border-radius: 110px 110px 0 0;
    background: linear-gradient(90deg, #7d7d80 0%, #6a6a6c 50%, var(--photo-tone) 50%, #5f6a2c 100%);
  }
  .portrait__base {
    position: absolute; left: 46px; top: 602px; width: 312px; height: 14px;
    border-radius: 50%; background: #0d0d0d;
  }
  .headline {
    position: absolute; left: 70px; top: 626px;
    font-family: "Bebas Neue", sans-serif; font-weight: 400;
    font-size: 100px; line-height: 84px; color: var(--navy);
    letter-spacing: 0.5px;
  }
  .quote {
    position: absolute; left: 62px; top: 893px; width: 340px;
    font-size: 15.5px; line-height: 20px; color: var(--ink);
  }
  .brand {
    position: absolute; left: 510px; top: 906px;
    font-size: 40px; font-weight: 700; color: var(--navy); letter-spacing: -1px;
    line-height: 48px;
  }
  .brand__tagline {
    position: absolute; left: 511px; top: 958px;
    font-size: 16px; font-weight: 500; color: var(--navy);
  }
</style>
</head>
<body>
  <main class="poster">
    <div class="poster__glow"></div>

    <div class="side-band side-band--navy"></div>
    <div class="side-band side-band--green"></div>

    <div class="side-link side-link--one">
      <span class="side-link__dot"></span>
      <span class="side-link__text">www.kelvabank.com</span>
    </div>
    <div class="side-link side-link--two">
      <span class="side-link__dot"></span>
      <span class="side-link__text">www.kelvabank.com</span>
    </div>

    <div class="portrait" role="img" aria-label="Photo of a smiling businesswoman with curly hair in an olive blazer, arms crossed, half shown in greyscale"></div>
    <div class="portrait__base"></div>

    <h1 class="headline">Banking<br>Has<br>Evolved</h1>

    <p class="quote">“My bank has to be there for me in ways<br>I cannot even imagine yet. My future is<br>bright and I need my bank to grow with<br>me. This One Bank is the only one I need”.</p>

    <p class="brand">KelvaBank</p>
    <p class="brand__tagline">Your bank, changing for you</p>
  </main>
</body>
</html>
```